Business card

I have changed logo's and colors. I have uploaded the new logo and colors.

In my head I am thinking about the main logo and text beside logo to be on one side of the card. The other side of the card to have just my picture and contact information.

The "R" emblem and the "equal housing" emblem... cut he MLS from the "R". and remove the wording from the house emblem.

Info on Card:

Wes Trundell
Designated Broker, CDPE, CNE, GRI
Direct: 602.555.0143
Fax: 623.555.0198
Wes@TrundellandAssociates.example
www.TrundellandAssociates.example
4193 North Sagebend Lane Glendale, AZ 85308

Please see brief as I have uploaded a new logo and a few notes.

Reason: I changed the logo and colors. Please see brief

I am leaning towards maybe a black business card(or at least on the front where the logo is). I liked several designs that were submitted. Please re-submit.

House

```html
<!DOCTYPE html>
<html lang="en">
<head>
<meta charset="utf-8">
<title>Trundell &amp; Associates – Business Card</title>
<link rel="stylesheet" href="https://fonts.googleapis.com/css2?family=Jost:wght@400&family=Source+Sans+3:wght@400;600&display=swap">
<style>
  :root {
    --navy: #3a4862;
    --orange: #d9782d;
    --charcoal: #3d3d42;
    --paper: #ffffff;
    --backdrop: #e6e6e8;
    --ink-light: #f2f2f2;
  }
  * { box-sizing: border-box; margin: 0; padding: 0; }
  html, body { width: 1200px; height: 720px; overflow: hidden; }
  body {
    background: var(--backdrop);
    font-family: "Source Sans 3", sans-serif;
    position: relative;
  }
  .card {
    position: absolute;
    top: 205px;
    width: 540px;
    height: 309px;
    background: var(--paper);
    border-radius: 4px;
    box-shadow: 0 10px 28px rgba(0,0,0,0.18);
    overflow: hidden;
  }
  .card--contact { left: 40px; }
  .card--brand { left: 620px; }

  /* wordmark */
  .wordmark {
    display: flex;
    align-items: center;
    font-family: "Jost", sans-serif;
    font-weight: 400;
    color: var(--navy);
    letter-spacing: 0.04em;
    line-height: 1;
    white-space: nowrap;
  }
  .wordmark__dot {
    border-radius: 50%;
    background: var(--navy);
    flex: none;
  }
  .card--brand .wordmark {
    position: absolute;
    left: 50%;
    top: 50%;
    transform: translate(-50%, -50%);
    font-size: 28px;
    gap: 14px;
  }
  .card--brand .wordmark__dot { width: 56px; height: 56px; }

  /* contact side */
  .card__shapes { position: absolute; inset: 0; }
  .card--contact .wordmark {
    position: absolute;
    left: 180px;
    top: 18px;
    font-size: 21px;
    gap: 9px;
  }
  .card--contact .wordmark__dot { width: 40px; height: 40px; }

  .person {
    position: absolute;
    left: 200px;
    top: 70px;
    color: var(--navy);
  }
  .person__name { font-size: 20px; font-weight: 600; line-height: 1.1; }
  .person__title { font-size: 12.5px; line-height: 1.3; }

  .badges {
    position: absolute;
    left: 40px;
    top: 72px;
    display: flex;
    gap: 6px;
  }
  .badge {
    width: 16px;
    height: 16px;
    border: 1.5px solid var(--orange);
    border-radius: 3px;
  }
  .badge--wide { width: 28px; background: var(--orange); }

  .contact {
    position: absolute;
    left: 20px;
    top: 198px;
    color: var(--ink-light);
    font-size: 11.5px;
    line-height: 1.6;
    list-style: none;
  }
  .contact__address { font-weight: 600; margin-bottom: 2px; }
  .contact__row { display: flex; align-items: center; gap: 6px; }
  .contact__row svg { width: 11px; height: 11px; flex: none; }
  .contact__gap { margin-left: 10px; }

  .portrait {
    position: absolute;
    right: 0;
    bottom: 0;
    width: 240px;
    height: 180px;
    background: linear-gradient(180deg, #f4efec 0%, #d8c3b7 38%, #3a3b41 60%, #2f3036 100%);
  }
</style>
</head>
<body>

  <section class="card card--contact" aria-label="Contact side">
    <svg class="card__shapes" viewBox="0 0 540 309" preserveAspectRatio="none" aria-hidden="true">
      <path d="M0 96 C180 86 318 165 364 309 L0 309 Z" fill="var(--orange)"/>
      <path d="M0 110 C170 100 300 170 345 309 L0 309 Z" fill="var(--charcoal)"/>
    </svg>

    <div class="portrait" role="img" aria-label="Portrait photo of the broker in a dark suit and mint tie"></div>

    <div class="wordmark">
      <span class="wordmark__dot"></span>
      <span class="wordmark__text">TRUNDELL &amp; ASSOCIATES</span>
    </div>

    <div class="badges" aria-hidden="true">
      <span class="badge"></span>
      <span class="badge badge--wide"></span>
      <span class="badge"></span>
    </div>

    <div class="person">
      <p class="person__name">Wes Trundell</p>
      <p class="person__title">Designated Broker CDPE, CNE, GRI</p>
    </div>

    <ul class="contact">
      <li class="contact__address">4193 North Sagebend Lane Glendale AZ 85308</li>
      <li class="contact__row">
        <svg viewBox="0 0 12 12"><path d="M2 1h3l1 3-2 1a7 7 0 0 0 3 3l1-2 3 1v3c-6 0-9-3-9-9z" fill="var(--orange)"/></svg>
        602.555.0143
        <svg class="contact__gap" viewBox="0 0 12 12"><rect x="3" y="1" width="6" height="4" fill="var(--orange)"/><rect x="1" y="5" width="10" height="6" rx="1" fill="var(--orange)"/></svg>
        623.555.0198
      </li>
      <li class="contact__row">
        <svg viewBox="0 0 12 12"><rect x="1" y="2.5" width="10" height="7" fill="none" stroke="var(--orange)"/><path d="M1 2.5l5 4 5-4" fill="none" stroke="var(--orange)"/></svg>
        Wes@TrundellandAssociates.example
      </li>
      <li class="contact__row">
        <svg viewBox="0 0 12 12"><circle cx="6" cy="6" r="5" fill="none" stroke="var(--orange)"/><path d="M1 6h10M6 1c-3 3-3 7 0 10M6 1c3 3 3 7 0 10" fill="none" stroke="var(--orange)" stroke-width="0.8"/></svg>
        www.TrundellandAssociates.example
      </li>
    </ul>
  </section>

  <section class="card card--brand" aria-label="Brand side">
    <div class="wordmark">
      <span class="wordmark__dot"></span>
      <span class="wordmark__text">TRUNDELL &amp; ASSOCIATES</span>
    </div>
  </section>

</body>
</html>
```